Business IT Services Billboard to attract local small businesses

We are Brivolane, a premier Managed Service Provider (MSP) specializing in comprehensive IT services and VOIP phone solutions exclusively for businesses. Our goal is to create a dynamic and visually engaging billboard advertisement that not only highlights our cutting-edge IT solutions but also emphasizes our state-of-the-art VOIP phone services. This billboard should communicate our commitment to providing innovative, reliable, and holistic technology solutions.
Target Market(s)
small business
Industry/Entity Type
Information Technology
Colors
Designer to choose colors to be used in the design.
Look and feel
Each slider illustrates characteristics of the customer's brand and the style your logo design should communicate.

```html
<!DOCTYPE html>
<html lang="en">
<head>
<meta charset="utf-8">
<title>Brivolane Billboard</title>
<link rel="stylesheet" href="https://fonts.googleapis.com/css2?family=Open+Sans:wght@600;700;800&display=swap">
<style>
  :root {
    --page-bg: #e6e7ea;
    --board-white: #f7f7f7;
    --band-dark: #231f1e;
    --ink: #1c1a19;
    --accent-blue: #1e76c4;
    --text-light: #ffffff;
    --globe-tone: #d9dadc;
    --headset-tone: #bfc2c6;
  }
  * { margin: 0; padding: 0; box-sizing: border-box; }
  html, body {
    width: 1200px; height: 1200px; overflow: hidden;
    background: var(--page-bg);
    font-family: "Open Sans", Arial, sans-serif;
  }
  .canvas {
    position: relative; width: 1200px; height: 1200px;
    display: flex; align-items: center; justify-content: center;
  }
  .billboard {
    position: relative; width: 1200px; height: 440px;
    background: var(--board-white); overflow: hidden;
  }
  .globe-art {
    position: absolute; left: 110px; top: 10px; width: 240px; height: 240px;
    border-radius: 50%;
    background: radial-gradient(circle at 40% 40%, #eeeeef 0%, var(--globe-tone) 70%, rgba(217,218,220,0) 100%);
  }
  .headline {
    position: absolute; left: 40px; top: 55px;
    color: var(--ink); font-weight: 800; text-transform: uppercase;
    line-height: 1.08; letter-spacing: 0.5px;
  }
  .headline .line-one { display: block; font-size: 46px; padding-left: 140px; }
  .headline .line-two { display: block; font-size: 50px; }
  .tagline {
    position: absolute; left: 40px; top: 188px;
    font-size: 24px; font-weight: 700; color: var(--ink);
  }
  .dark-band {
    position: absolute; left: 0; top: 228px; width: 100%; height: 212px;
    background: var(--band-dark);
  }
  .cta-pill {
    position: absolute; left: 330px; top: 252px;
    background: var(--accent-blue); color: var(--text-light);
    font-size: 22px; font-weight: 700; padding: 3px 14px; border-radius: 3px;
  }
  .web-address {
    position: absolute; left: 210px; top: 300px;
    font-size: 56px; font-weight: 700; color: var(--text-light); letter-spacing: 0.5px;
  }
  .headset-art {
    position: absolute; right: 60px; top: 90px; width: 120px; height: 220px;
    border-radius: 50px 50px 20px 20px;
    background: linear-gradient(180deg, #e3e4e6 0%, var(--headset-tone) 100%);
  }
  .brand-mark {
    position: absolute; right: 40px; bottom: 34px;
    display: flex; align-items: center; gap: 10px;
  }
  .brand-mark .brand-square { width: 22px; height: 22px; background: var(--accent-blue); }
  .brand-mark .brand-name { font-size: 28px; font-weight: 700; color: var(--text-light); }
</style>
</head>
<body>
  <main class="canvas">
    <section class="billboard">
      <div class="globe-art" role="img" aria-label="Faint globe with network arcs"></div>
      <h1 class="headline">
        <span class="line-one">Seamless Technology</span>
        <span class="line-two">Solutions for Modern Businesse</span>
      </h1>
      <p class="tagline">Innovative IT and VOIP Solutions Tailored for Your Business Success</p>
      <div class="dark-band"></div>
      <p class="cta-pill">Transform Your Tech Today</p>
      <p class="web-address">www.brivolane.com</p>
      <div class="headset-art" role="img" aria-label="Office phone headset with microphone"></div>
      <div class="brand-mark">
        <span class="brand-square"></span>
        <span class="brand-name">Brivolane</span>
      </div>
    </section>
  </main>
</body>
</html>
```